Sticker label design for - Tidal Fern Deodorant Balm

I need a label for my 100% Natural Deodorant Balm
The brand is called "Plum Meadow Brand", and the product is called TIDAL FERN Deodorant Balm.
There are two labels, one is a 5.2cm circle for the top, and 4.5cm circle for the base. The jar is amber plastic with black lid.
Width: 5.8cm
Height: 3.4cm (Lid 1.2cm, base 2,2cm)
Here is a link to what the jar looks like from one of my competitors: https://copperwren.com.au/products/body/velaro-deodorant-paste/
The product is a unisex product. Please see uploaded files for designs previously made for the brand. I'm trying to see a few more designs before finalising my choice. Feel free to use the logo at the top (Plum Meadow Brand) of either attachment if you would like. Or design your own.
Be be aware that it is meant to be Aluminium and Paraben Free, not "Parabens" Weight of product is 70g, please include this.
Label can be any colour, and printed with regular colours or event gold, silver or rose gold foil. Would a background be nice?
This is something I saw that I liked:
http://www.mossvelbalm.com
However I'm really open to what people can come up with.
For the back base-
Tidal Fern deodorant balm is made from 100% natural ingredients, and works by neutralises odour and minimising wetness without the use of harmful chemicals.
www.plummeadowbrand.com
Directions: For optimal result, apply a pea size amount of the balm to your dry armpits. Gently rub the balm into your armpits covering the entire area. Discontinue use if irritation occurs.
Ingredients: Shea Butter, Coconut oil, Sodium Bicarbonate, Arrowroot, Kaolin Clay, Vitamin E, Vegetable Glycerin, Activated Charcoal, Essential oils of Peppermint, Lavender, Mandarin, Tea tree, Geranium Rose & Cedarwood.
MADE IN AUSTRALIA
Reason: Hi,
I'm not getting many submissions, so was hoping to extend the deadline.
Skin Care Product

```html
<!DOCTYPE html>
<html lang="en">
<head>
<meta charset="UTF-8">
<title>Tidal Fern Deodorant Balm – Side Label</title>
<link rel="stylesheet" href="https://fonts.googleapis.com/css2?family=Russo+One&family=Arimo:wght@400&family=Open+Sans:wght@600&display=swap">
<style>
  :root {
    --page-bg: #ffffff;
    --label-edge: #3b3744;
    --label-centre: #5b5566;
    --label-text: #ffffff;
    --label-soft-text: #e4e2e8;
    --brand-text: #d9d7de;
    --claim-text: #bdb9c6;
    --rule-line: #7a7486;
    --accent-green: #4caf50;
  }
  * { margin: 0; padding: 0; box-sizing: border-box; }
  html, body {
    width: 1200px;
    height: 1200px;
    overflow: hidden;
    background: var(--page-bg);
  }
  .canvas {
    width: 1200px;
    height: 1200px;
    display: flex;
    align-items: center;
    justify-content: center;
  }
  .side-label {
    width: 1000px;
    height: 540px;
    background: linear-gradient(90deg, var(--label-edge) 0%, var(--label-centre) 45%, var(--label-edge) 100%);
    display: flex;
    flex-direction: column;
    align-items: center;
    justify-content: center;
  }
  .brand-mark {
    width: 26px;
    height: 26px;
    border-radius: 50%;
    background: var(--accent-green);
    margin-bottom: 34px;
  }
  .brand-name {
    font-family: "Open Sans", sans-serif;
    font-weight: 600;
    font-size: 30px;
    letter-spacing: 0.42em;
    color: var(--brand-text);
    text-transform: lowercase;
    margin-bottom: 38px;
    padding-left: 0.42em;
  }
  .product-name {
    font-family: "Russo One", sans-serif;
    font-size: 100px;
    line-height: 1;
    letter-spacing: 0.04em;
    color: var(--label-text);
  }
  .product-type {
    font-family: "Arimo", sans-serif;
    font-weight: 400;
    font-size: 46px;
    letter-spacing: 0.06em;
    color: var(--label-soft-text);
    margin-top: 6px;
  }
  .label-footer {
    margin-top: 34px;
    padding-top: 18px;
    width: 560px;
    border-top: 1px solid var(--rule-line);
    display: flex;
    justify-content: space-between;
    font-family: "Arimo", sans-serif;
    font-size: 22px;
    letter-spacing: 0.14em;
    color: var(--claim-text);
    text-transform: uppercase;
  }
  .net-weight { text-transform: none; }
</style>
</head>
<body>
  <main class="canvas">
    <section class="side-label">
      <span class="brand-mark" aria-hidden="true"></span>
      <p class="brand-name">plum meadow brand</p>
      <h1 class="product-name">TIDAL FERN</h1>
      <p class="product-type">DEODORANT BALM</p>
      <footer class="label-footer">
        <span class="free-from">Aluminium &amp; Paraben Free</span>
        <span class="net-weight">70g</span>
      </footer>
    </section>
  </main>
</body>
</html>
```